Real Estate Business Cards

Looking for a clean, sharp and professional look for our Real Estate investment Fund that invests in Multi Family Apartment buildings.

Target Market(s)

Real Estate Fund

Industry/Entity Type

Real Estate

Contact Information for Business Card

Company Description: Real Estate Investment Fund
Company Name: RKW Holdings
Name: Marcus Olvane
Cell: (917) 482-0657
Email: marcus@rkwholdings-example.com
Website: www.rkwholdings-example.com
Address: 418, 9th Street, Brooklyn NY 11218

Colors

Designer to choose colors to be used in the design.

Requirements
Nice to have
• Colors to match logo

```html
<!DOCTYPE html>
<html lang="en">
<head>
<meta charset="utf-8">
<title>RKW Holdings – Business Card</title>
<link rel="stylesheet" href="https://fonts.googleapis.com/css2?family=Hind:wght@600&family=Questrial&display=swap">
<style>
  :root {
    --brand-blue: #1572ab;
    --ink-grey: #4a4a4a;
    --card-white: #ffffff;
    --backdrop: #d6d6d6;
  }
  * { box-sizing: border-box; margin: 0; padding: 0; }
  html, body {
    width: 1125px; height: 1200px; overflow: hidden;
    background: var(--backdrop);
  }
  .canvas { position: relative; width: 1125px; height: 1200px; }

  .card {
    position: absolute; left: 178px; width: 768px; height: 436px;
    border-radius: 24px; overflow: hidden;
  }
  .card--front { top: 140px; background: var(--card-white); }
  .card--back  { top: 626px; background: var(--brand-blue); }

  .wordmark {
    position: absolute; left: 35px; top: 76px;
    display: flex; align-items: center; gap: 14px;
    font-family: "Questrial", sans-serif; font-size: 34px;
    color: var(--brand-blue); letter-spacing: 1px;
  }
  .wordmark__square {
    width: 26px; height: 26px; background: var(--brand-blue);
  }

  .holder {
    position: absolute; right: 37px; top: 236px; text-align: right;
  }
  .holder__name {
    font-family: "Hind", sans-serif; font-weight: 600;
    font-size: 25px; line-height: 1; color: var(--brand-blue);
    letter-spacing: 0.3px;
  }
  .holder__role {
    margin-top: 6px;
    font-family: "Questrial", sans-serif; font-size: 18px; line-height: 1;
    color: var(--ink-grey);
  }
  .divider {
    position: absolute; left: 35px; top: 274px; width: 647px; height: 2px;
    background: var(--brand-blue);
  }
  .edge-tab {
    position: absolute; right: 0; top: 241px; width: 12px; height: 43px;
    background: var(--brand-blue); border-radius: 8px 0 0 8px;
  }

  .contacts {
    position: absolute; left: 35px; top: 318px; list-style: none;
    font-family: "Questrial", sans-serif; font-size: 18.5px; color: var(--ink-grey);
  }
  .contacts__item {
    display: flex; align-items: center; height: 30px;
  }
  .contacts__icon { width: 14px; height: 14px; margin-right: 10px; flex: none; }
  .contacts__accent { color: var(--brand-blue); }

  .address {
    position: absolute; right: 37px; top: 354px; text-align: right;
    font-family: "Questrial", sans-serif; font-size: 18.5px; line-height: 23px;
    color: var(--ink-grey); font-style: normal;
  }
  .base-band {
    position: absolute; left: 0; bottom: 0; width: 100%; height: 11px;
    background: var(--brand-blue);
  }

  .back-name {
    position: absolute; inset: 0;
    display: flex; align-items: center; justify-content: center;
    font-family: "Questrial", sans-serif; font-size: 38px; letter-spacing: 1px;
    color: var(--card-white);
  }
</style>
</head>
<body>
<main class="canvas">

  <section class="card card--front" aria-label="Business card front">
    <div class="wordmark">
      <span class="wordmark__square" aria-hidden="true"></span>
      <span class="wordmark__name">RKW Holdings</span>
    </div>

    <div class="holder">
      <p class="holder__name">MARCUS OLVANE</p>
      <p class="holder__role">CEO</p>
    </div>
    <div class="divider"></div>
    <div class="edge-tab"></div>

    <ul class="contacts">
      <li class="contacts__item">
        <svg class="contacts__icon" viewBox="0 0 24 24" aria-hidden="true">
          <path fill="#1572ab" d="M6.6 10.8a15 15 0 0 0 6.6 6.6l2.2-2.2a1 1 0 0 1 1-.25 11.4 11.4 0 0 0 3.6.57 1 1 0 0 1 1 1V20a1 1 0 0 1-1 1A17 17 0 0 1 3 4a1 1 0 0 1 1-1h3.5a1 1 0 0 1 1 1c0 1.25.2 2.45.57 3.57a1 1 0 0 1-.25 1z"/>
        </svg>
        (917) 482-0657
      </li>
      <li class="contacts__item">
        <svg class="contacts__icon" viewBox="0 0 24 24" aria-hidden="true">
          <rect x="2" y="5" width="20" height="14" fill="#1572ab"/>
          <path d="M5 8l7 5 7-5" fill="none" stroke="#fff" stroke-width="2"/>
        </svg>
        marcus@rkwholdings-example.com
      </li>
      <li class="contacts__item">
        <svg class="contacts__icon" viewBox="0 0 24 24" aria-hidden="true">
          <circle cx="12" cy="12" r="10" fill="#1572ab"/>
          <path d="M2 12h20M12 2c3 3 3 17 0 20M12 2c-3 3-3 17 0 20" fill="none" stroke="#fff" stroke-width="1.5"/>
        </svg>
        www.<span class="contacts__accent">rkwholdings-example</span>.com
      </li>
    </ul>

    <address class="address">418, 9th Street,<br>Brooklyn NY 11218</address>
    <div class="base-band"></div>
  </section>

  <section class="card card--back" aria-label="Business card back">
    <div class="back-name">RKW Holdings</div>
  </section>

</main>
</body>
</html>
```